Package Design for 15 lines of Tea

I need design variations for 15 different Tea lines.
The tea will be packaged in Tin cylinders.
I have attached several pictures to show you an example of the display we are modelling after along with other references.
The 15 tea lines are:
Study Tea
Ingredients: Brazilian Mate, Mint
Energy Boost Tea
Ingredients: Yunnan Coffee, Dark Puer
Relaxation Tea
Ingredients: Lotus Flower, South African Rooibos
Beauty Tea
Ingredients: Rose, Chrysanthemum, Red Dates, Huangqi
Sore Throat Tea
Ingredients: Honeysuckle, Pang Da Hai, Chamomile, Licorice Root
Get Well Tea
Ingredients: Ginger, Rooibos, Orange peel, Chinese Angelica
Diet Tea
Ingredients: Puer, Hibiscus, Lemongrass, Lotus Plumule
Bedtime Tea
Ingredients: Apple, Orange, Chamomile
South African Rooibos Tea
(pure)
Brazilian Yerba Mate Tea
(pure)
Long Jing Green Tea
(pure)
Darjeeling Black Tea
(pure)
Nepal Golden Tea
(Pure)
Bai Mu Dan White Tea
(pure)
Phoenix Oolong Tea
(pure)
Every Tea Blend should have three unique symbols that describe the purpose and theme of the blend. (!!Please don't make specific reference to the ingredients of the blends because some of these ingredients may be changed later. Stick to focusing on the intended purpose of the tea blend!!)
I would like the symbols to keep the same brushlike style that is consistent with our company logo.
Please keep the three block structure. I suggest keeping to just one color per tea blend. This will help each blend stand out between one another. I have a sample of the "Diet Tea" attached that I did myself to give you an idea of the structure I'm looking for, but obviously it's just my amateur version. Hope you can make them look far more appealing.
The ultimate goal is to build a picture language unique to our brand. As more products are released, we intend to potentially have hundreds of symbols, each with it's own meaning. So it would be nice when you present your pictures if you explain its intended meaning or message.
Deminsions:
Cylinder type 1: 82mm*38mmH
circular labels (along with your design) will be placed on the cap of product, and then the cylinder will be slanted on it's side to display the cap towards the customer.
Cylinder type 2: 65mm*152mmH
the labels will be placed on the side of the cylinder. In this version, try lining the three symbols in a vertical position. If this looks awful to you then feel free to go back to the horizontal style, but it would be nice to see what the vertical version looks like for reference.
Updates
Due to the scope of this project, please take note that I just increased my budget an additional 500 dollars more.
I also just added a 100 dollar second place prize. Don't want to see hard work unrewarded.
Feel free to send a few samples and I will provide prompt feedback. Please don't feel that you must submit all 15 lines at the same time.
Reason: I am extending the deadline as I feel there are more detailed revisions that need to be made until final selection.
Target Market(s)
Middle to Upper Class Consumers in China
Industry/Entity Type
It Company
Font styles to use
Other font styles liked:
- font similar to font on company logo
Requirements
Must have
- Tea Designs must be in harmony with company logo and theme.
Should not have
- Avoid using Chinese characters as symbols. They may seem cool to westerners, but it's tacky for Chinese consumers.

```html
<!DOCTYPE html>
<html lang="en">
<head>
<meta charset="utf-8">
<title>Mixed Tea Set – Cap Labels</title>
<link rel="stylesheet" href="https://fonts.googleapis.com/css2?family=Special+Elite&family=Courier+Prime&family=Josefin+Slab:wght@300;400&display=swap">
<style>
  :root {
    --page-bg: #f4f4f4;
    --caption: #4a4a4a;
    --ink-black: #0b0b0b;
    --silver-light: #f0f0f0;
    --silver-dark: #c4c4c4;
    --relax-light: #8fd3f0;
    --relax-dark: #3fa4d2;
    --beauty-light: #c3dd3c;
    --beauty-dark: #97b821;
    --bedtime-light: #ffc04a;
    --bedtime-dark: #ee8f12;
    --energy: #e6a21f;
    --getwell: #b5c532;
    --diet: #2f8fca;
    --sore: #e0561d;
    --label-size: 240px;
  }
  * { box-sizing: border-box; margin: 0; padding: 0; }
  html, body { width: 1200px; height: 1000px; overflow: hidden; }
  body {
    background: var(--page-bg);
    font-family: "Courier Prime", "Courier New", monospace;
    position: relative;
  }
  .set-title {
    position: absolute; left: 58px; top: 58px;
    font-family: "Josefin Slab", Georgia, serif;
    font-weight: 300; font-size: 24px; color: var(--caption);
  }
  .range {
    position: absolute; left: 45px; width: 1110px;
  }
  .range--supporting { top: 140px; }
  .range--active { top: 540px; }
  .range-caption {
    font-family: "Josefin Slab", Georgia, serif;
    font-weight: 300; font-size: 24px; color: var(--caption);
    margin-bottom: 22px;
  }
  .label-row { display: flex; justify-content: space-between; }
  .cap-label {
    width: var(--label-size); height: var(--label-size);
    border-radius: 50%;
    display: flex; flex-direction: column; align-items: center;
    padding-top: 44px;
    box-shadow: 0 0 0 6px #8f8f8f, 0 8px 18px rgba(0,0,0,.25);
  }
  .tea-name {
    font-family: "Special Elite", "Courier New", monospace;
    font-size: 19px; line-height: 20px; text-align: center;
    color: var(--ink-black);
  }
  .symbols { display: flex; gap: 6px; margin-top: 12px; }
  .symbol {
    width: 50px; height: 52px; display: block;
    background: var(--ink-black);
  }
  .symbol:nth-child(1) { transform: rotate(-3deg); }
  .symbol:nth-child(2) { transform: rotate(1deg); }
  .symbol:nth-child(3) { transform: rotate(3deg); }
  .ingredients {
    margin-top: 12px; font-size: 9.5px; line-height: 11px;
    text-align: center; color: #4c4c4c; max-width: 150px;
  }

  .cap-label--study { background: radial-gradient(circle at 40% 35%, var(--silver-light), var(--silver-dark)); }
  .cap-label--relaxation { background: radial-gradient(circle at 40% 35%, var(--relax-light), var(--relax-dark)); }
  .cap-label--beauty { background: radial-gradient(circle at 40% 35%, var(--beauty-light), var(--beauty-dark)); }
  .cap-label--bedtime { background: radial-gradient(circle at 40% 35%, var(--bedtime-light), var(--bedtime-dark)); }
  .cap-label--bedtime .ingredients { color: #6a3a00; }
  .cap-label--relaxation .ingredients { color: #1d4e66; }
  .cap-label--beauty .ingredients { color: #3d4c0a; }

  .cap-label--active { background: var(--ink-black); }
  .cap-label--energy .symbol { background: var(--energy); }
  .cap-label--energy .tea-name { color: #f2f2f2; }
  .cap-label--energy .ingredients { color: #8a5f12; }
  .cap-label--getwell .symbol { background: var(--getwell); }
  .cap-label--getwell .tea-name { color: var(--getwell); }
  .cap-label--getwell .ingredients { color: #6b7420; }
  .cap-label--diet .symbol { background: var(--diet); }
  .cap-label--diet .tea-name { color: var(--diet); }
  .cap-label--diet .ingredients { color: #1e5a80; }
  .cap-label--sore .symbol { background: var(--sore); }
  .cap-label--sore .tea-name { color: var(--sore); }
  .cap-label--sore .ingredients { color: #8a3612; }
</style>
</head>
<body>
  <h1 class="set-title">Mixed TEA set</h1>

  <section class="range range--supporting">
    <h2 class="range-caption">Supporting TEA (color)</h2>
    <div class="label-row">
      <div class="cap-label cap-label--study">
        <p class="tea-name">Study<br>Tea</p>
        <div class="symbols">
          <span class="symbol" role="img" aria-label="Brush symbol: mug"></span>
          <span class="symbol" role="img" aria-label="Brush symbol: open book"></span>
          <span class="symbol" role="img" aria-label="Brush symbol: speech bubble"></span>
        </div>
        <p class="ingredients">Ingredients:<br>Brazilian Mate,<br>Mint</p>
      </div>
      <div class="cap-label cap-label--relaxation">
        <p class="tea-name">Relaxation<br>Tea</p>
        <div class="symbols">
          <span class="symbol" role="img" aria-label="Brush symbol: jagged wave"></span>
          <span class="symbol" role="img" aria-label="Brush symbol: soft wave"></span>
          <span class="symbol" role="img" aria-label="Brush symbol: calm line"></span>
        </div>
        <p class="ingredients">Ingredients:<br>Lotus Flower,<br>South African Rooibos</p>
      </div>
      <div class="cap-label cap-label--beauty">
        <p class="tea-name">Beauty<br>Tea</p>
        <div class="symbols">
          <span class="symbol" role="img" aria-label="Brush symbol: flower"></span>
          <span class="symbol" role="img" aria-label="Brush symbol: heart"></span>
          <span class="symbol" role="img" aria-label="Brush symbol: butterfly"></span>
        </div>
        <p class="ingredients">Ingredients:<br>Rose, Chrysanthemum,<br>Red Dates, Huangqi</p>
      </div>
      <div class="cap-label cap-label--bedtime">
        <p class="tea-name">Bedtime<br>Tea</p>
        <div class="symbols">
          <span class="symbol" role="img" aria-label="Brush symbol: setting sun"></span>
          <span class="symbol" role="img" aria-label="Brush symbol: crescent moon"></span>
          <span class="symbol" role="img" aria-label="Brush symbol: stars"></span>
        </div>
        <p class="ingredients">Ingredients:<br>Apple,<br>Orange,<br>Chamomile</p>
      </div>
    </div>
  </section>

  <section class="range range--active">
    <h2 class="range-caption">Active TEA (black)</h2>
    <div class="label-row">
      <div class="cap-label cap-label--active cap-label--energy">
        <p class="tea-name">Energy Boost<br>Tea</p>
        <div class="symbols">
          <span class="symbol" role="img" aria-label="Brush symbol: rising stroke"></span>
          <span class="symbol" role="img" aria-label="Brush symbol: rising stroke"></span>
          <span class="symbol" role="img" aria-label="Brush symbol: rising stroke"></span>
        </div>
        <p class="ingredients">Ingredients:<br>Yunnan Coffee,<br>Dark Puer</p>
      </div>
      <div class="cap-label cap-label--active cap-label--getwell">
        <p class="tea-name">Get Well<br>Tea</p>
        <div class="symbols">
          <span class="symbol" role="img" aria-label="Brush symbol: apple"></span>
          <span class="symbol" role="img" aria-label="Brush symbol: figure with raised arms"></span>
          <span class="symbol" role="img" aria-label="Brush symbol: sun"></span>
        </div>
        <p class="ingredients">Ingredients:<br>Ginger, Rooibos,<br>Orange peel,<br>Chinese Angelica</p>
      </div>
      <div class="cap-label cap-label--active cap-label--diet">
        <p class="tea-name">Diet<br>Tea</p>
        <div class="symbols">
          <span class="symbol" role="img" aria-label="Brush symbol: three flowing lines"></span>
          <span class="symbol" role="img" aria-label="Brush symbol: two flowing lines"></span>
          <span class="symbol" role="img" aria-label="Brush symbol: one flowing line"></span>
        </div>
        <p class="ingredients">Ingredients:<br>Puer, Hibiscus,<br>Lemongrass,<br>Lotus Plumule</p>
      </div>
      <div class="cap-label cap-label--active cap-label--sore">
        <p class="tea-name">Sore Throat<br>Tea</p>
        <div class="symbols">
          <span class="symbol" role="img" aria-label="Brush symbol: large flame"></span>
          <span class="symbol" role="img" aria-label="Brush symbol: smaller flame"></span>
          <span class="symbol" role="img" aria-label="Brush symbol: fading ember"></span>
        </div>
        <p class="ingredients">Ingredients:<br>Honeysuckle,<br>Pang Da Hai, Chamomile,<br>Licorice Root</p>
      </div>
    </div>
  </section>
</body>
</html>
```